I would like to modify/update my 2 step login screen

I want a more modern looking login page for our document imaging application. I need to keep all of the same elements and buttons that currently exist. The first 2 screens are the login. The 3rd is a screenshot of the actual application home page.

```html
<!DOCTYPE html>
<html lang="en">
<head>
<meta charset="utf-8">
<title>Northbeam Partners – Login and Dashboard Screens</title>
<link href="https://fonts.googleapis.com/css2?family=Inter:wght@400;500;600&display=swap" rel="stylesheet">
<style>
:root{
  --stage:#b3b3b3;
  --brand:#0a45f0;
  --brand-2:#0a7cf5;
  --btn:#1f6ff2;
  --ink:#111418;
  --muted:#8a93a3;
  --faint:#c9ced8;
  --line:#d9dde5;
  --white:#ffffff;
  --soft:#eef3fc;
  --cal:#e7eefb;
  --row-head:#f1f3f7;
  --illus-a:#4f86ff;
  --illus-b:#1c57f2;
  --alert:#ef4b5a;
}
*{box-sizing:border-box;margin:0;padding:0}
html,body{width:779px;height:1200px;overflow:hidden}
body{background:var(--stage);font-family:'Inter',sans-serif;color:var(--ink);position:relative}
.screen{position:absolute;left:65px;width:649px;height:346px;overflow:hidden;background:
  radial-gradient(ellipse 90px 55px at 420px 0px,rgba(90,160,255,.55),transparent 70%),
  radial-gradient(ellipse 110px 80px at 640px 340px,rgba(80,150,255,.6),transparent 70%),
  linear-gradient(90deg,#fff 40%,#f4f8ff 100%)}
.screen.app{background:
  radial-gradient(ellipse 120px 60px at 120px 0px,rgba(90,160,255,.5),transparent 70%),
  radial-gradient(ellipse 110px 70px at 620px 340px,rgba(80,150,255,.55),transparent 70%),
  var(--soft)}
.abs{position:absolute}
.hero-panel{left:0;top:26px;width:267px;height:295px;background:var(--brand);border-radius:0 15px 15px 0}
.hero-panel .ground{left:0;top:235px;width:267px;height:1px;background:rgba(255,255,255,.35)}
.brand-mark{display:flex;align-items:center;gap:4px;color:var(--white);font-weight:600;font-size:9px;letter-spacing:.3px}
.brand-mark .dot{width:10px;height:10px;background:var(--white);border-radius:2px}
.illustration{left:33px;top:64px;width:194px;height:197px;border-radius:50% 50% 12px 12px;
  background:radial-gradient(circle at 55% 35%,var(--illus-a),var(--illus-b) 70%)}
.heading{font-size:15px;font-weight:500;line-height:1.2}
.label{font-size:5.5px;font-weight:500}
.field{width:153px;height:13px;border:.6px solid var(--line);border-radius:2px;background:var(--white);font-size:4.5px;color:var(--faint);padding:0 4px;display:flex;align-items:center}
.sso{width:75px;height:13px;border:.6px solid var(--line);border-radius:2px;background:var(--white);font-size:4.6px;display:flex;align-items:center;gap:3px;padding-left:6px}
.sso.primary{border-color:#4c9a52}
.sso i{width:6px;height:6px;display:block;border-radius:50%;background:#2b2f36}
.sso i.sq{border-radius:1px;background:#f25022}
.note{font-size:5.3px}
.note a{color:var(--btn);text-decoration:none;font-weight:500}
.btn{height:13px;width:75px;border-radius:2px;font-size:5px;display:flex;align-items:center;justify-content:center}
.btn.fill{background:var(--btn);color:var(--white)}
.btn.line{border:.7px solid #333;background:var(--white)}
.sidebar{left:0;top:26px;width:90px;height:295px;background:var(--brand);border-radius:0 15px 15px 0;color:var(--white)}
.nav-item{display:flex;align-items:center;gap:5px;font-size:6.2px;left:18px}
.nav-item svg{width:9px;height:9px}
.card{background:var(--white);border-radius:3px}
.card-title{font-size:6.2px;font-weight:500}
.mini-btn{height:11px;width:27px;border-radius:2px;background:var(--brand-2);color:var(--white);font-size:4.2px;display:flex;align-items:center;justify-content:center}
.mini-btn.pale{background:#4aa0f7}
.thead{height:14px;background:var(--row-head);border-radius:2px;font-size:4px;color:#444;font-weight:500;letter-spacing:.2px}
.thead span,.row span{position:absolute;top:50%;transform:translateY(-50%);white-space:nowrap}
.row{height:8px;font-size:4.4px;color:var(--muted)}
.create-card{background:var(--brand-2);border-radius:3px;color:var(--white)}
.create-card .thead{background:var(--white)}
.create-card .row{color:var(--white)}
.create-card .mini-btn{background:#1f6ff2}
.cal-card{background:var(--cal);border-radius:3px}
.chip{height:8px;padding:0 4px;background:var(--white);border-radius:4px;font-size:3.8px;display:flex;align-items:center}
.cal-text{font-size:3.8px;transform:translate(-50%,-50%);white-space:nowrap}
.cal-text.dim{color:var(--faint)}
.cal-sel{width:8px;height:8px;border-radius:2px;background:var(--brand-2);color:var(--white);display:flex;align-items:center;justify-content:center}
.axis{font-size:2.8px;color:var(--muted);transform:translate(-50%,-50%)}
.badge{width:16px;height:16px;border-radius:5px;display:flex;align-items:center;justify-content:center}
.badge b{position:absolute;top:-3px;right:-3px;width:6px;height:6px;border-radius:50%;font-size:3px;color:#fff;display:flex;align-items:center;justify-content:center;font-weight:500}
</style>
</head>
<body>

<!-- Screen 1: SSO login -->
<section class="screen" style="top:62px">
  <div class="abs hero-panel">
    <div class="abs brand-mark" style="left:25px;top:28px"><span class="dot"></span>NORTHBEAM PARTNERS</div>
    <div class="abs illustration" role="img" aria-label="Illustration of a person thinking beside a chart easel, gears, documents and a potted plant"></div>
    <div class="abs ground"></div>
  </div>
  <h1 class="abs heading" style="left:373px;top:80px">Welcome back!</h1>
  <h2 class="abs heading" style="left:373px;top:101px">NBSS Login</h2>
  <div class="abs label" style="left:373px;top:131px">Database</div>
  <div class="abs field" style="left:373px;top:139px">Enter Your Database</div>
  <div class="abs sso primary" style="left:373px;top:162px">Sign in with MyNBView</div>
  <div class="abs sso" style="left:451px;top:162px"><i></i>Sign in with Orbitly</div>
  <div class="abs sso" style="left:373px;top:178px"><i class="sq"></i>Sign in with Tessera</div>
  <div class="abs sso" style="left:451px;top:178px"><i></i>Sign in with KeyPass</div>
  <p class="abs note" style="left:373px;top:199px">Don't have an account?&nbsp; <a href="#">SignUp</a></p>
</section>

<!-- Screen 2: classic login -->
<section class="screen" style="top:427px">
  <div class="abs hero-panel">
    <div class="abs brand-mark" style="left:25px;top:28px"><span class="dot"></span>NORTHBEAM PARTNERS</div>
    <div class="abs illustration" role="img" aria-label="Illustration of a person thinking beside a chart easel, gears, documents and a potted plant"></div>
    <div class="abs ground"></div>
  </div>
  <h1 class="abs heading" style="left:373px;top:101px">Classic Login</h1>
  <div class="abs label" style="left:373px;top:130px">Username</div>
  <div class="abs field" style="left:373px;top:139px">Your Name Here</div>
  <div class="abs label" style="left:373px;top:158px">Password</div>
  <div class="abs field" style="left:373px;top:167px">Your Password Here</div>
  <div class="abs" style="left:450px;width:76px;top:184px;font-size:4.2px;text-align:right">Forgot Password</div>
  <div class="abs btn fill" style="left:373px;top:201px">Log in</div>
  <div class="abs btn line" style="left:451px;top:201px">Sign Up</div>
</section>

<!-- Screen 3: dashboard -->
<section class="screen app" style="top:793px">
  <nav class="abs sidebar">
    <div class="abs" style="left:16px;top:37px;font-size:9.5px;font-weight:500">Dana Reyes</div>
    <div class="abs nav-item" style="top:66px"><svg viewBox="0 0 10 10" fill="none" stroke="#fff" stroke-width=".8"><rect x="1" y="2" width="8" height="7" rx="1"/><path d="M1 4h8M3 1v2M7 1v2"/></svg>Timesheets</div>
    <div class="abs nav-item" style="top:91px"><svg viewBox="0 0 10 10" fill="none" stroke="#fff" stroke-width=".8"><path d="M2 8l3-6 3 6z"/><circle cx="5" cy="6" r="1"/></svg>NBSupport</div>
    <div class="abs nav-item" style="top:117px"><svg viewBox="0 0 10 10" fill="none" stroke="#fff" stroke-width=".8"><rect x="2" y="1" width="6" height="8" rx="1"/><path d="M3.5 4h3M3.5 6h3"/></svg>Requistions</div>
    <div class="abs nav-item" style="top:142px"><svg viewBox="0 0 10 10" fill="none" stroke="#fff" stroke-width=".8"><rect x="1" y="1" width="8" height="8" rx="1"/><circle cx="4.5" cy="4.5" r="1.6"/><path d="M5.7 5.7l1.8 1.8"/></svg>Record Search</div>
    <div class="abs nav-item" style="top:167px"><svg viewBox="0 0 10 10" fill="none" stroke="#fff" stroke-width=".8"><circle cx="5" cy="5" r="3.5"/><circle cx="5" cy="5" r="1.3"/></svg>Workflow</div>
    <div class="abs nav-item" style="top:193px"><svg viewBox="0 0 10 10" fill="none" stroke="#fff" stroke-width=".8"><path d="M1 9h8M2.5 9V6M5 9V3.5M7.5 9V5"/></svg>Expenses</div>
    <div class="abs brand-mark" style="left:18px;top:250px;font-size:7px"><span class="dot" style="width:8px;height:8px"></span>NORTHBEAM</div>
  </nav>

  <header>
    <h1 class="abs" style="left:115px;top:26px;font-size:11px;font-weight:500">Dashboard</h1>
    <p class="abs" style="left:115px;top:40px;font-size:6px;color:var(--muted)">Hi, Dana. Welcome back&nbsp; to NBAdmin!</p>
    <div class="abs badge" style="left:514px;top:29px;background:#d6e6ff"><svg width="8" height="8" viewBox="0 0 10 10" fill="none" stroke="#1f6ff2" stroke-width=".9"><path d="M2.5 7.5V5a2.5 2.5 0 015 0v2.5H2.5zM4 9h2"/></svg><b style="background:var(--brand-2)">21</b></div>
    <div class="abs badge" style="left:536px;top:29px;background:#fbdde0"><svg width="8" height="8" viewBox="0 0 10 10" fill="none" stroke="#ef4b5a" stroke-width=".9"><circle cx="5" cy="5" r="1.4"/><circle cx="5" cy="5" r="3.3" stroke-dasharray="1.2 .9"/></svg><b style="background:var(--alert)">19</b></div>
    <div class="abs" style="left:562px;top:28px;width:.6px;height:18px;background:var(--line)"></div>
    <div class="abs" style="left:568px;top:34px;font-size:5.5px">Hello, <b style="font-weight:600">Dana</b></div>
    <div class="abs" role="img" aria-label="User profile photo" style="left:603px;top:28px;width:18px;height:18px;border-radius:50%;background:linear-gradient(#c79a7c,#6b4a3a);border:1px solid #fff"></div>
  </header>

  <!-- My Forms -->
  <div class="abs card" style="left:115px;top:66px;width:314px;height:126px">
    <div class="abs card-title" style="left:8px;top:10px">My Forms</div>
    <div class="abs mini-btn pale" style="left:249px;top:10px">Edit Form</div>
    <div class="abs mini-btn" style="left:279px;top:10px">Create</div>
    <div class="abs" style="left:8px;top:22px;width:113px;border-bottom:.5px solid var(--line);font-size:3px;color:var(--faint);padding-bottom:1px">Search here</div>
    <div class="abs thead" style="left:8px;top:32px;width:297px"><span style="left:7px">TYPE</span><span style="left:110px;color:var(--muted)">DESCRIPTION</span><span style="left:241px;color:var(--muted)">CREATED DATE</span></div>
    <div class="abs row" style="left:8px;top:55px;width:297px"><span style="left:7px">Your Product Title Here</span><span style="left:110px">Lorem Ipsum is simply dummy text of printing.</span><span style="left:241px">10/18/2024</span></div>
    <div class="abs row" style="left:8px;top:67px;width:297px"><span style="left:7px">Your Product Title Here</span><span style="left:110px">Lorem Ipsum is simply dummy text of printing.</span><span style="left:241px">10/18/2024</span></div>
    <div class="abs row" style="left:8px;top:80px;width:297px"><span style="left:7px">Your Product Title Here</span><span style="left:110px">Lorem Ipsum is simply dummy text of printing.</span><span style="left:241px">10/18/2024</span></div>
    <div class="abs row" style="left:8px;top:92px;width:297px"><span style="left:7px">Your Product Title Here</span><span style="left:110px">Lorem Ipsum is simply dummy text of printing.</span><span style="left:241px">10/18/2024</span></div>
    <div class="abs row" style="left:8px;top:105px;width:297px"><span style="left:7px">Your Product Title Here</span><span style="left:110px">Lorem Ipsum is simply dummy text of printing.</span><span style="left:241px">10/18/2024</span></div>
  </div>

  <!-- Create Forms -->
  <div class="abs create-card" style="left:434px;top:66px;width:187px;height:126px">
    <div class="abs card-title" style="left:8px;top:10px">Create Forms</div>
    <div class="abs mini-btn" style="left:148px;top:10px">Create</div>
    <div class="abs thead" style="left:8px;top:27px;width:167px"><span style="left:7px">TYPE</span><span style="left:107px;color:var(--muted)">DESCRIPTION</span></div>
    <div class="abs row" style="left:8px;top:51px;width:167px"><span style="left:7px">Your Product Title Here</span><span style="left:107px">Description goes here.</span></div>
    <div class="abs row" style="left:8px;top:63px;width:167px"><span style="left:7px">Your Product Title Here</span><span style="left:107px">Description goes here.</span></div>
    <div class="abs row" style="left:8px;top:76px;width:167px"><span style="left:7px">Your Product Title Here</span><span style="left:107px">Description goes here.</span></div>
    <div class="abs row" style="left:8px;top:88px;width:167px"><span style="left:7px">Your Product Title Here</span><span style="left:107px">Description goes here.</span></div>
    <div class="abs row" style="left:8px;top:101px;width:167px"><span style="left:7px">Your Product Title Here</span><span style="left:107px">Description goes here.</span></div>
  </div>

  <!-- Calendar -->
  <div class="abs cal-card" style="left:115px;top:198px;width:117px;height:126px">
    <div class="abs card-title" style="left:7px;top:6px">Calendar</div>
    <div class="abs chip" style="left:7px;top:17px">Today</div>
    <div class="abs chip" style="left:27px;top:17px">Last 7 days</div>
    <div class="abs chip" style="left:57px;top:17px">Last month</div>
    <div class="abs" style="left:95px;top:17px;width:8px;height:8px;border-radius:50%;background:#fff"></div>
    <div class="abs" style="left:7px;top:32px;width:103px;border-top:.5px solid var(--line)"></div>
  </div>
  <div class="abs cal-text" style="left:126px;top:236px">Su</div><div class="abs cal-text" style="left:137px;top:236px">Mo</div><div class="abs cal-text" style="left:149px;top:236px">Tu</div><div class="abs cal-text" style="left:160px;top:236px">We</div><div class="abs cal-text" style="left:172px;top:236px">Th</div><div class="abs cal-text" style="left:183px;top:236px">Fr</div><div class="abs cal-text" style="left:195px;top:236px">Sa</div>
  <div class="abs cal-text dim" style="left:126px;top:247px">27</div><div class="abs cal-text dim" style="left:137px;top:247px">28</div><div class="abs cal-text dim" style="left:149px;top:247px">1</div><div class="abs cal-text dim" style="left:160px;top:247px">2</div><div class="abs cal-text dim" style="left:172px;top:247px">3</div><div class="abs cal-text dim" style="left:183px;top:247px">4</div><div class="abs cal-text dim" style="left:195px;top:247px">5</div>
  <div class="abs cal-text dim" style="left:126px;top:258px">6</div><div class="abs cal-text dim" style="left:137px;top:258px">7</div><div class="abs cal-text dim" style="left:149px;top:258px">8</div><div class="abs cal-text dim" style="left:160px;top:258px">9</div><div class="abs cal-text dim" style="left:172px;top:258px">10</div><div class="abs cal-text dim" style="left:183px;top:258px">11</div><div class="abs cal-text dim" style="left:195px;top:258px">12</div>
  <div class="abs cal-text dim" style="left:126px;top:270px">13</div><div class="abs cal-text cal-sel" style="left:137px;top:270px">14</div><div class="abs cal-text" style="left:149px;top:270px">15</div><div class="abs cal-text" style="left:160px;top:270px">16</div><div class="abs cal-text" style="left:172px;top:270px">17</div><div class="abs cal-text" style="left:183px;top:270px">18</div><div class="abs cal-text" style="left:195px;top:270px">19</div>
  <div class="abs cal-text" style="left:126px;top:281px">20</div><div class="abs cal-text" style="left:137px;top:281px">21</div><div class="abs cal-text" style="left:149px;top:281px">22</div><div class="abs cal-text" style="left:160px;top:281px">23</div><div class="abs cal-text" style="left:172px;top:281px">24</div><div class="abs cal-text" style="left:183px;top:281px">25</div><div class="abs cal-text" style="left:195px;top:281px">26</div>
  <div class="abs cal-text" style="left:126px;top:293px">27</div><div class="abs cal-text" style="left:137px;top:293px">28</div><div class="abs cal-text" style="left:149px;top:293px">29</div><div class="abs cal-text" style="left:160px;top:293px">30</div><div class="abs cal-text" style="left:172px;top:293px">31</div><div class="abs cal-text dim" style="left:183px;top:293px">1</div><div class="abs cal-text dim" style="left:195px;top:293px">2</div>
  <div class="abs cal-text dim" style="left:214px;top:241px;font-size:2.6px">Jun</div>
  <div class="abs cal-text" style="left:214px;top:248px;font-size:3.2px;color:var(--muted)">May</div>
  <div class="abs cal-text" style="left:214px;top:255px;color:var(--muted)">Apr</div>
  <div class="abs cal-text" style="left:214px;top:264px;font-size:4.4px;font-weight:500">Mar</div>
  <div class="abs" style="left:206px;top:260px;width:16px;border-top:.4px solid var(--line)"></div>
  <div class="abs" style="left:206px;top:268px;width:16px;border-top:.4px solid var(--line)"></div>
  <div class="abs cal-text" style="left:214px;top:275px;color:var(--muted)">Feb</div>
  <div class="abs cal-text dim" style="left:214px;top:282px;font-size:3.2px">Jan</div>
  <div class="abs cal-text dim" style="left:214px;top:289px;font-size:2.6px">Dec</div>
  <div class="abs chip" style="left:184px;top:303px;font-size:3.6px;color:var(--muted)">Clear</div>
  <div class="abs chip" style="left:205px;top:303px;width:20px;justify-content:center;background:var(--brand-2);color:#fff;font-size:3.6px">Apply</div>

  <!-- Work Flow Summary -->
  <div class="abs card" style="left:238px;top:198px;width:206px;height:126px">
    <div class="abs card-title" style="left:8px;top:6px">Work Flow Summary</div>
    <div class="abs thead" style="left:8px;top:21px;width:188px"><span style="left:7px">TYPE</span><span style="left:161px;color:var(--muted)">ITEMS</span></div>
    <div class="abs row" style="left:8px;top:43px;width:188px"><span style="left:7px">Lorem Ipsum is simply dummy text of printing.</span><span style="left:161px">3</span></div>
    <div class="abs row" style="left:8px;top:55px;width:188px"><span style="left:7px">Lorem Ipsum is simply dummy text of printing.</span><span style="left:161px">5</span></div>
    <div class="abs row" style="left:8px;top:68px;width:188px"><span style="left:7px">Lorem Ipsum is simply dummy text of printing.</span><span style="left:161px">1</span></div>
    <div class="abs row" style="left:8px;top:80px;width:188px"><span style="left:7px">Lorem Ipsum is simply dummy text of printing.</span><span style="left:161px">2</span></div>
    <div class="abs row" style="left:8px;top:93px;width:188px"><span style="left:7px">Lorem Ipsum is simply dummy text of printing.</span><span style="left:161px">4</span></div>
    <div class="abs row" style="left:8px;top:105px;width:188px"><span style="left:7px">Lorem Ipsum is simply dummy text of printing.</span><span style="left:161px">7</span></div>
  </div>

  <!-- Expenses -->
  <div class="abs card" style="left:450px;top:198px;width:172px;height:126px">
    <div class="abs card-title" style="left:11px;top:6px">Expenses</div>
    <svg class="abs" style="left:20px;top:50px" width="140" height="50" viewBox="0 0 140 50" fill="none">
      <path d="M2 42 C8 30,12 28,16 38 S24 48,32 38 S48 30,56 36 S66 46,72 30 S82 12,90 20 S96 34,102 26 S112 14,118 22 S126 34,132 24 L136 22 V50 H2Z" fill="#f1f3f6"/>
      <path d="M2 42 C8 30,12 28,16 38 S24 48,32 38 S48 30,56 36 S66 46,72 30 S82 12,90 20 S96 34,102 26 S112 14,118 22 S126 34,132 24 L136 22" stroke="#2b2f36" stroke-width=".6"/>
      <path d="M2 38 C20 30,40 34,60 28 S100 22,118 14 L136 4" stroke="#b9bfca" stroke-width=".4" stroke-dasharray="1 1"/>
    </svg>
  </div>
  <div class="abs axis" style="left:466px;top:224px">50K</div>
  <div class="abs axis" style="left:466px;top:237px">40K</div>
  <div class="abs axis" style="left:466px;top:250px">30K</div>
  <div class="abs axis" style="left:466px;top:265px">20K</div>
  <div class="abs axis" style="left:466px;top:280px">10K</div>
  <div class="abs axis" style="left:468px;top:294px">0</div>
  <div class="abs axis" style="left:483px;top:304px">Jan</div><div class="abs axis" style="left:502px;top:304px">Feb</div><div class="abs axis" style="left:522px;top:304px">Mar</div><div class="abs axis" style="left:542px;top:304px">Apr</div><div class="abs axis" style="left:562px;top:304px">May</div><div class="abs axis" style="left:582px;top:304px">Jun</div><div class="abs axis" style="left:601px;top:304px">Jul</div>
</section>

</body>
</html>
```